Web Design Project

Dear designer(s),

I need a design for a shop who's specialized into...

-Material to fix or do tailor made clothing (cloth, buttons, zippers etc)
-Curtains (static/pull-up)
-Blinds (plastic/wood)

that kind of stuff.

Good thing is that I can provide a lot of pretty photo's to work with. I have 3.5 Gigabyte of 300-1200 dpi photo's altho I converted most of them to 72dpi for your convenience (75Mb).

You can download the working material from this quillbarn link:

http://files.quillbarn.net/u/31862094/Velunor.zip

this is an updated file, it contains the dutch menu items to use in your design

http://files.quillbarn.net/u/31862094/Velunor_Content.txt

Notice: take your time to come up with something nice. I prefer 1 or 2 designs from a designer that has been thinked of, than 5 quick ones.
Updates

Thank you for those who posted designs already but I want to clarify something.

As I mentioned it's a shop, that's a physical shop and not a webshop.

So you can safe some time and skip drawing the shopping cart icons, shop items on the homepage and other shop related things.

They don't want to start online reselling as they already spend most of their time in their shop to catch up with all orders.

Keep up the good work!

Industry/Entity Type

Clothing

Requirements
Nice to have
• Maybe the hi-res pictures can be used as background ratotor that appears left/right next to the centered website content?

Since there is a lot of material each section might have his topic linked set of thumbnails that opens a bigger image on clicking?

```html
<!DOCTYPE html>
<html lang="en">
<head>
<meta charset="utf-8">
<title>Velunor – Fabrics, Table Linen &amp; Window Dressing</title>
<link href="https://fonts.googleapis.com/css2?family=Arimo:wght@400;700&family=Gelasio:wght@400&display=swap" rel="stylesheet">
<style>
:root{
  --page:#f2f2f2;
  --panel:#ffffff;
  --ink:#333333;
  --muted:#8a8a8a;
  --soft:#666666;
  --blue:#1f7ac4;
  --brand:#1f6fb5;
  --navy:#0f3d66;
  --line:#d8d8d8;
  --card:#f0f0f0;
  --footer:#2c2c2c;
  --footer-deep:#222222;
  --footer-text:#b9b9b9;
  --footer-line:#454545;
}
*{margin:0;padding:0;box-sizing:border-box}
html,body{width:745px;height:1200px;overflow:hidden}
body{background:var(--page);font-family:"Arimo",Arial,sans-serif;color:var(--ink);position:relative}
.abs{position:absolute}
.serif{font-family:"Gelasio",Georgia,serif;font-weight:400}

/* header */
.site-header{left:71px;top:57px;width:603px;height:64px;background:var(--panel)}
.brand{left:14px;top:20px;font-size:19px;font-weight:700;color:var(--brand);letter-spacing:-.3px}
.brand-url{left:90px;top:42px;font-size:9px;color:var(--soft)}
.main-nav{left:250px;top:25px;display:flex;align-items:center;font-size:8.5px;color:var(--ink)}
.main-nav span{padding:4px 6px;margin-right:8px;border-radius:10px;border:1px solid transparent}
.main-nav .active{border-color:var(--line);background:#f6f6f6;padding:4px 9px}

/* slider */
.hero{left:71px;top:121px;width:603px;height:260px;overflow:hidden}
.hero-photo{width:100%;height:100%;background:
  linear-gradient(90deg,#bfb9ad 0%,#a89f8f 18%,#3a3350 27%,#4b3f72 33%,#d9c36a 40%,#ecebe4 48%,#eeeeea 58%,#93b043 62%,#9fbd4c 74%,#c23b8c 82%,#b83381 100%);}
.hero-photo::after{content:"";position:absolute;left:0;right:0;bottom:0;height:45%;
  background:linear-gradient(180deg,rgba(205,203,198,.0),rgba(200,198,192,.95) 40%,#b9b6b0)}
.hero-caption{left:0;top:82px;width:186px;height:64px;background:rgba(18,118,200,.92);color:#fff}
.hero-caption h1{position:absolute;left:13px;top:5px;font-size:17px;font-weight:400;font-family:"Arimo",Arial,sans-serif}
.hero-caption p{position:absolute;left:13px;top:25px;font-size:10.5px}
.hero-btn{position:absolute;left:13px;top:41px;background:var(--navy);color:#fff;font-size:7px;font-weight:700;padding:4px 5px}
.dots{right:10px;bottom:7px;display:flex;gap:4px}
.dots i{width:8px;height:8px;border-radius:50%;background:#3a3a3a;border:1px solid #666;display:block}
.dots i.on{background:var(--blue)}

.intro{left:71px;top:381px;width:603px;height:59px;background:var(--panel)}
.intro .lead{position:absolute;left:13px;top:16px;font-size:11px;color:#444}
.intro .lead em{font-style:normal;color:var(--blue)}
.intro .sub{position:absolute;left:13px;top:33px;font-size:7.5px;color:var(--muted)}

/* about + news */
.panel{background:var(--panel)}
.info{left:71px;top:453px;width:603px;height:214px}
.sec-title{display:flex;align-items:center;font-size:14px;color:#333}
.sec-title::after{content:"";flex:1;height:1px;background:var(--line);margin-left:8px}
.about-title{left:13px;top:16px;width:216px}
.news-title{left:259px;top:16px;width:331px}
.about-brand{left:13px;top:59px;font-size:17px;font-weight:700;color:#555}
.about-url{left:92px;top:77px;font-size:9.5px;color:#555}
.about-text{left:13px;top:101px;width:218px;font-size:7.8px;line-height:11.6px;color:var(--soft);text-align:justify}
.readmore{left:13px;top:167px;width:58px;height:19px;border:1px solid var(--line);border-radius:10px;font-size:7.8px;color:#444;display:flex;align-items:center;justify-content:center;background:#fafafa}
.news{left:260px;width:331px}
.news .cal{position:absolute;left:0;top:-4px}
.news .txt{position:absolute;left:36px;top:0;font-size:7.8px;color:#444}
.news .by{position:absolute;left:36px;top:13px;font-size:6.6px;color:var(--muted)}
.news .by b{font-weight:400;color:var(--blue)}
.news .cm{position:absolute;left:36px;top:25px;font-size:6.6px;color:var(--muted);font-style:italic}
.divider{left:260px;width:331px;border-top:1px dotted #cfcfcf}

/* products */
.products{left:71px;top:680px;width:603px;height:280px}
.prod-title{left:13px;top:14px;width:578px}
.filters{left:13px;top:37px;font-size:7.8px;color:var(--muted)}
.filters b{font-weight:400;color:var(--blue)}
.filters i{font-style:normal;margin:0 4px;color:#bbb}
.card{top:64px;width:187px;height:191px;background:var(--card)}
.card .photo{height:128px}
.card h3{position:absolute;left:8px;top:138px;font-size:10.5px;color:#333}
.card p{position:absolute;left:8px;top:153px;width:170px;font-size:6.6px;line-height:10px;color:var(--muted)}

/* footer */
.site-footer{left:0;top:983px;width:745px;height:159px;background:var(--footer)}
.foot-title{font-size:10.5px;color:#ddd}
.foot-title::after{background:var(--footer-line)}
.contact-list{left:71px;top:53px;font-size:7.8px;color:var(--footer-text);line-height:17.4px}
.contact-list b{font-weight:400;color:#eee}
.cat-list{left:291px;top:56px;list-style:none;font-size:7.8px;color:var(--footer-text);line-height:17.2px}
.cat-list li{display:flex;align-items:center;gap:5px}
.cat-list li.on{color:var(--blue)}
.news-sign{left:488px;top:57px;font-size:7.8px;color:var(--footer-text)}
.news-input{left:488px;top:76px;width:185px;height:16px;background:#262626;border:1px solid #3d3d3d;font-size:6.6px;color:#6d6d6d;padding:3px 5px}
.news-btn{left:488px;top:102px;width:43px;height:14px;background:#3a4652;border:1px solid #556170;color:#e5e5e5;font-size:7px;display:flex;align-items:center;justify-content:center}
.foot-bar{left:0;top:1142px;width:745px;height:58px;background:var(--footer-deep)}
.foot-links{left:71px;top:29px;font-size:7.8px;color:var(--footer-text)}
.foot-links i{font-style:normal;margin:0 4px}
.copy{right:71px;top:29px;font-size:7.8px;color:var(--footer-text)}
.up{left:362px;top:-7px;width:20px;height:14px;border-radius:10px 10px 0 0;background:var(--footer-deep)}
</style>
</head>
<body>

<header class="site-header abs">
  <div class="brand abs">Velunor</div>
  <div class="brand-url abs">www.velunor.be</div>
  <nav class="main-nav abs">
    <span>Home</span><span>Cloth - Fabric</span><span class="active">Table cloth</span><span>Decoration cloth</span><span>Pull systems</span><span>Contact</span>
  </nav>
</header>

<section class="hero abs">
  <div class="hero-photo" role="img" aria-label="Living room with a grey sofa, a bright pink plaid throw and colourful purple, yellow, green and magenta linen curtains"></div>
  <div class="hero-caption abs">
    <h1>Your Edition 2013</h1>
    <p>Classic Appeal &amp; Style</p>
    <span class="hero-btn">View collection »</span>
  </div>
  <div class="dots abs"><i></i><i class="on"></i><i></i><i></i></div>
</section>

<section class="intro abs">
  <p class="lead serif">Lorem Ipsum is simply dummy text of the <em>printing</em> and typesetting industry.</p>
  <p class="sub">It is a long established fact that a reader will be distracted by the readable content of a page when looking at its layout</p>
</section>

<section class="info panel abs">
  <h2 class="sec-title serif about-title abs">About us</h2>
  <div class="about-brand abs">Velunor</div>
  <div class="about-url abs">www.velunor.be</div>
  <p class="about-text abs">Contrary to popular belief, Lorem Ipsum is not simply random text. It has roots in a piece of classical Latin literature from 45 BC, making it over 2000 years old. Edwin Harlowe, a Latin professor at Ashford-Lynne College in Virginia.</p>
  <span class="readmore abs">Readmore</span>

  <h2 class="sec-title serif news-title abs">Latest News</h2>

  <div class="news abs" style="top:51px">
    <svg class="cal" width="24" height="28" viewBox="0 0 24 28"><rect x=".5" y=".5" width="23" height="27" fill="#fff" stroke="#555"/><rect x=".5" y=".5" width="23" height="7" fill="#555"/><text x="12" y="6" font-size="4.5" fill="#fff" text-anchor="middle" font-family="Arimo,sans-serif" font-weight="700">MAR</text><text x="12" y="23" font-size="13" fill="#333" text-anchor="middle" font-family="Gelasio,serif">28</text></svg>
    <p class="txt">Lorem Ipsum is simply dummy text of the printing and typesetting industry.</p>
    <p class="by">Posted by <b>Dorian Vell</b></p>
    <p class="cm">123 comments</p>
  </div>
  <div class="divider abs" style="top:91px"></div>
  <div class="news abs" style="top:107px">
    <svg class="cal" width="24" height="28" viewBox="0 0 24 28"><rect x=".5" y=".5" width="23" height="27" fill="#fff" stroke="#555"/><rect x=".5" y=".5" width="23" height="7" fill="#555"/><text x="12" y="6" font-size="4.5" fill="#fff" text-anchor="middle" font-family="Arimo,sans-serif" font-weight="700">MAR</text><text x="12" y="23" font-size="13" fill="#333" text-anchor="middle" font-family="Gelasio,serif">16</text></svg>
    <p class="txt">Lorem Ipsum is simply dummy text of the printing.</p>
    <p class="by">Posted by <b>Marcus Tarrow</b></p>
    <p class="cm">83 comments</p>
  </div>
  <div class="divider abs" style="top:144px"></div>
  <div class="news abs" style="top:160px">
    <svg class="cal" width="24" height="28" viewBox="0 0 24 28"><rect x=".5" y=".5" width="23" height="27" fill="#fff" stroke="#555"/><rect x=".5" y=".5" width="23" height="7" fill="#555"/><text x="12" y="6" font-size="4.5" fill="#fff" text-anchor="middle" font-family="Arimo,sans-serif" font-weight="700">MAR</text><text x="12" y="23" font-size="13" fill="#333" text-anchor="middle" font-family="Gelasio,serif">12</text></svg>
    <p class="txt">Lorem Ipsum is simply dummy text of the printing and typesetting.</p>
    <p class="by">Posted by <b>Leon Bravik</b></p>
    <p class="cm">568 comments</p>
  </div>
</section>

<section class="products panel abs">
  <h2 class="sec-title serif prod-title abs">Our Products</h2>
  <p class="filters abs">Cloth - Fabric<i>/</i><b>Table cloth</b><i>/</i>Decoration cloth<i>/</i>Pull systems</p>

  <article class="card abs" style="left:13px">
    <div class="photo" role="img" aria-label="Bright room with wooden venetian blinds and a white arc floor lamp" style="background:linear-gradient(90deg,#8a6a4c,#c9b7a2 45%,#e8e6e2 70%,#d7d3cd)"></div>
    <h3 class="serif">Lorem Ipsum is simply dummy text</h3>
    <p>It is a long established fact that a reader will be distracted by the readable content...</p>
  </article>
  <article class="card abs" style="left:208px">
    <div class="photo" role="img" aria-label="Dining room with sheer white curtains and a white table set" style="background:linear-gradient(90deg,#7e8a70,#cfd1cb 35%,#eeeeec 60%,#b9b6b0)"></div>
    <h3 class="serif">Lorem Ipsum is simply dummy text</h3>
    <p>It is a long established fact that a reader will be distracted by the readable content...</p>
  </article>
  <article class="card abs" style="left:403px">
    <div class="photo" role="img" aria-label="Table dressed with a grey striped tablecloth, green plates and a vase of flowers" style="background:linear-gradient(180deg,#cfc3d4,#ddd6e0 35%,#a7aab8 60%,#8f94a5)"></div>
    <h3 class="serif">Lorem Ipsum is simply dummy text</h3>
    <p>It is a long established fact that a reader will be distracted by the readable content...</p>
  </article>
</section>

<footer class="site-footer abs">
  <h3 class="sec-title serif foot-title abs" style="left:71px;top:36px;width:168px">Contact us</h3>
  <div class="contact-list abs">
    <p><b>Phone:</b> 4-512-7 (845-310-2764)</p>
    <p><b>Email:</b> info@velunor.be</p>
    <p><b>Address:</b> 27 Linden Weave Street</p>
    <p>Harlow Creek, OR 97341</p>
    <p>USA</p>
  </div>

  <h3 class="sec-title serif foot-title abs" style="left:291px;top:36px;width:168px">Categories</h3>
  <ul class="cat-list abs">
    <li><svg width="6" height="6" viewBox="0 0 6 6"><path d="M.5 3l1.8 1.8L5.5 1" fill="none" stroke="#aaa" stroke-width="1"/></svg>Cloth - Fabric</li>
    <li class="on"><svg width="6" height="6" viewBox="0 0 6 6"><path d="M.5 3l1.8 1.8L5.5 1" fill="none" stroke="#aaa" stroke-width="1"/></svg>Table cloth</li>
    <li><svg width="6" height="6" viewBox="0 0 6 6"><path d="M.5 3l1.8 1.8L5.5 1" fill="none" stroke="#aaa" stroke-width="1"/></svg>Decoration cloth</li>
    <li><svg width="6" height="6" viewBox="0 0 6 6"><path d="M.5 3l1.8 1.8L5.5 1" fill="none" stroke="#aaa" stroke-width="1"/></svg>Pull systems</li>
    <li><svg width="6" height="6" viewBox="0 0 6 6"><path d="M.5 3l1.8 1.8L5.5 1" fill="none" stroke="#aaa" stroke-width="1"/></svg>Curtains</li>
  </ul>

  <h3 class="sec-title serif foot-title abs" style="left:488px;top:36px;width:186px">Our Newsletter</h3>
  <p class="news-sign abs">Sign Up for Our Newsletter</p>
  <div class="news-input abs">Your email address</div>
  <div class="news-btn abs">Subscribe</div>
</footer>

<div class="foot-bar abs">
  <div class="up abs"><svg width="20" height="14" viewBox="0 0 20 14"><path d="M7.5 9l2.5-2.5L12.5 9" fill="none" stroke="#777" stroke-width="1"/></svg></div>
  <p class="foot-links abs">About Us<i>|</i>Customer Service<i>|</i>Site Map<i>|</i>Search Terms<i>|</i>Contact Us</p>
  <p class="copy abs">© 2013 Velunor. All Rights Reserved.</p>
</div>

</body>
</html>
```